Brightwave Travel and Tours

Hotel Reservations
Airline Ticketing
Day Tour

My business is a Travel agency. My services are issuing domestic and international tickets. Book room/hotel reservations local/international.
My color preference is apple green/orange/red/blue.
Images of beaches, tickets,luggage.

```html
<!DOCTYPE html>
<html lang="en">
<head>
<meta charset="utf-8">
<title>Brightwave Travel and Tours – Business Card</title>
<link rel="stylesheet" href="https://fonts.googleapis.com/css2?family=Open+Sans:wght@400;600;700&display=swap">
<style>
  :root {
    --teal-deep: #0f7f9f;
    --teal: #1595b8;
    --cyan: #22c3e3;
    --white: #ffffff;
    --paper: #f5f6f6;
    --ink: #1d1d1f;
    --stage: #e7e9ea;
  }
  * { box-sizing: border-box; margin: 0; padding: 0; }
  html, body { width: 1200px; height: 780px; overflow: hidden; }
  body {
    background: var(--stage);
    font-family: "Open Sans", Arial, sans-serif;
    position: relative;
  }
  .card {
    position: absolute;
    top: 242px;
    width: 520px;
    height: 297px;
    border-radius: 16px;
    overflow: hidden;
    background: linear-gradient(180deg, var(--white), var(--paper));
    box-shadow: 0 3px 0 #d9dcdd, 0 6px 0 var(--teal), 0 14px 26px rgba(0,0,0,.18);
  }
  .card--front { left: 50px; }
  .card--back { left: 630px; }
  .card-art { position: absolute; inset: 0; width: 100%; height: 100%; }

  /* front */
  .brand {
    position: absolute; left: 34px; top: 78px;
    display: flex; align-items: center; gap: 14px;
  }
  .brand-dot {
    width: 58px; height: 58px; border-radius: 50%;
    background: var(--teal);
  }
  .brand-name {
    color: var(--teal); font-weight: 700; line-height: 1.05;
  }
  .brand-name .word { display: block; font-size: 30px; letter-spacing: 1px; }
  .brand-name .tag { display: block; font-size: 13px; letter-spacing: 2.2px; }

  .person {
    position: absolute; right: 28px; top: 22px; text-align: right;
  }
  .person-name { color: var(--teal); font-weight: 700; font-size: 20px; }
  .person-role { color: var(--ink); font-size: 12px; margin-top: -2px; }

  .contacts {
    position: absolute; right: 28px; top: 86px;
    list-style: none; text-align: right; font-size: 12.5px; color: var(--ink);
    line-height: 18px;
  }
  .contacts li { display: flex; justify-content: flex-end; align-items: center; gap: 8px; }
  .contacts .icon { width: 14px; height: 14px; }
  .contacts .web { color: var(--teal); }

  .address {
    position: absolute; right: 28px; bottom: 20px; text-align: right;
    color: var(--white); font-size: 13px; line-height: 17px;
  }

  /* back */
  .back-name {
    position: absolute; left: 0; right: 0; top: 92px; text-align: center;
    color: var(--teal); font-weight: 700; line-height: 1;
  }
  .back-name .word { display: block; font-size: 52px; letter-spacing: 2px; }
  .back-name .tag { display: block; font-size: 19px; letter-spacing: 4px; margin-top: 6px; }
  .services {
    position: absolute; left: 26px; bottom: 22px;
    color: var(--white); font-size: 14px; letter-spacing: .3px;
  }
</style>
</head>
<body>

<section class="card card--front" aria-label="Business card front">
  <svg class="card-art" viewBox="0 0 520 297" preserveAspectRatio="none" aria-hidden="true">
    <defs>
      <linearGradient id="frontBand" x1="0" y1="0" x2="1" y2="0">
        <stop offset="0" stop-color="#1ba7c9"/>
        <stop offset="1" stop-color="#0f7f9f"/>
      </linearGradient>
    </defs>
    <path d="M0,297 L0,282 C160,275 340,230 520,150 L520,297 Z" fill="url(#frontBand)"/>
    <path d="M40,272 C210,258 380,210 520,112 C390,200 220,250 40,272 Z" fill="#22c3e3"/>
    <path d="M0,292 C170,284 350,240 520,160 L520,166 C350,246 170,290 0,297 Z" fill="#ffffff" opacity=".55"/>
  </svg>

  <div class="brand">
    <span class="brand-dot"></span>
    <p class="brand-name"><span class="word">BRIGHTWAVE</span><span class="tag">TRAVEL AND TOURS</span></p>
  </div>

  <div class="person">
    <p class="person-name">Employee Name</p>
    <p class="person-role">Managing Director</p>
  </div>

  <ul class="contacts">
    <li>000.000.0000
      <svg class="icon" viewBox="0 0 14 14"><rect width="14" height="14" rx="2" fill="#22a9cf"/><path d="M4 3h2l1 2-1 1c.5 1 1.2 1.7 2 2l1-1 2 1v2c-4 0-7-3-7-7z" fill="#fff"/></svg>
    </li>
    <li>000.000.0000
      <svg class="icon" viewBox="0 0 14 14"><rect width="14" height="14" rx="2" fill="#22a9cf"/><rect x="4" y="3" width="6" height="8" rx="1" fill="#fff"/></svg>
    </li>
    <li>info@youremail.com
      <svg class="icon" viewBox="0 0 14 14"><rect width="14" height="14" rx="2" fill="#22a9cf"/><rect x="3" y="4" width="8" height="6" fill="#fff"/><path d="M3 4l4 3 4-3" stroke="#22a9cf" fill="none"/></svg>
    </li>
    <li class="web">www.yourwebsite.com</li>
  </ul>

  <p class="address">your address Rd., Suite 000<br>Harborview, USA</p>
</section>

<section class="card card--back" aria-label="Business card back">
  <svg class="card-art" viewBox="0 0 520 297" preserveAspectRatio="none" aria-hidden="true">
    <defs>
      <linearGradient id="backBand" x1="0" y1="0" x2="1" y2="0">
        <stop offset="0" stop-color="#0f7f9f"/>
        <stop offset="1" stop-color="#1ba7c9"/>
      </linearGradient>
    </defs>
    <path d="M0,0 H520 V82 C360,56 180,36 0,30 Z" fill="url(#backBand)"/>
    <path d="M60,52 C220,56 380,74 520,100 C380,80 220,64 60,52 Z" fill="#22c3e3"/>
    <path d="M0,297 V212 C170,236 350,258 520,268 V297 Z" fill="url(#backBand)"/>
    <path d="M0,198 C180,224 350,246 470,256 C350,252 170,234 0,206 Z" fill="#22c3e3"/>
  </svg>

  <p class="back-name"><span class="word">BRIGHTWAVE</span><span class="tag">TRAVEL AND TOURS</span></p>

  <p class="services">Hotel Reservations &nbsp;|&nbsp; Airline Ticketing &nbsp;|&nbsp; Day Tour</p>
</section>

</body>
</html>
```